Dog care service needs advertising poster

Our company is Paw Haven. We provide care for dogs while their owners are away, either through home visits or a holiday stay in the homes of carefully selected minders. Our existing website & Facebook cover should provide all the colour cues for a poster - namely blues, blondes and grey. We have an existing logo (provided). We can feature the same imagery from our website as I have purchased the rights to the stock images.

www.pawhavenexample.com.au
www.facebook.com/pawhavenexampleau

This brief is for design of a poster that can be placed in vet surgeries, groomers, on community noticeboards. It should be scalable to print in three sizes, A5, A4 & A3.

We wish to clearly communicate our three areas of service "dog minding, home visits, dog walking".

We would like to have the files ready for upload to Printora (or similar) for immediate printing.

Target Market(s)

Dog owners who love their dogs like family.

Industry/Entity Type

Advertising

Font styles to use
Sans Serif

Colors
33a6d7
3276b5

Requirements
Must have
• Logo
• www.pawhavenexample.com.au
• Telephone number
• Three services - Dog Minding, Home Visits, Dog Walking
Nice to have
• use of our existing stock photography to highlight the three areas of service - Dog minding, home visits, dog walking. Existing colour palette - blues, blondes and grey.
• Text that can be used:
• Western Sydney’s complete dog care service.
• Dog Minding - Your dog stays in the home of one of our carefully selected minders.Treated like part of the family, they enjoy all the creature comforts they are used to.
• Home Visits - We visit your dog at your home for feeding, walking and playtime. Short of long visits available.
• Dog Walking - If you can't walk your dog for any reason we are here to help. 1/2 hour or hourly walks available.
• Contact us today for a tailored package to meet your needs.
Should not have
• Any additional illustrations beyond the logo.

```html
<!DOCTYPE html>
<html lang="en">
<head>
<meta charset="utf-8">
<title>Paw Haven – Pet Services Poster</title>
<link href="https://fonts.googleapis.com/css2?family=Exo+2:wght@300;400;600;700;800&display=swap" rel="stylesheet">
<style>
  :root {
    --sky: #33a6d7;
    --ocean: #3276b5;
    --slate: #3a4554;
    --frame: #3b4453;
    --white: #ffffff;
    --grey-text: #4a90b8;
    --photo-green: #5f8a3e;
    --photo-blonde: #c9a77c;
    --photo-tan: #b48a5e;
  }
  * { margin: 0; padding: 0; box-sizing: border-box; }
  html, body { width: 872px; height: 1200px; overflow: hidden; background: var(--white); }
  .poster {
    position: relative;
    width: 872px;
    height: 1200px;
    font-family: "Exo 2", sans-serif;
    overflow: hidden;
  }
  .poster-bands { position: absolute; inset: 0; }
  .brand {
    position: absolute;
    left: 118px;
    top: 48px;
    display: flex;
    align-items: center;
    gap: 26px;
  }
  .brand-mark {
    width: 150px; height: 150px;
    border-radius: 50%;
    background: var(--slate);
  }
  .brand-text { display: flex; flex-direction: column; }
  .brand-name {
    font-weight: 600;
    font-size: 78px;
    line-height: 1;
    color: var(--slate);
    letter-spacing: -0.5px;
  }
  .brand-tagline {
    margin-top: 12px;
    font-weight: 600;
    font-size: 24px;
    letter-spacing: 10px;
    color: var(--sky);
    padding-left: 40px;
  }
  .service-photo {
    position: absolute;
    border-radius: 50%;
    border: 7px solid var(--frame);
    box-shadow: 0 8px 18px rgba(0,0,0,0.35);
  }
  .photo-minding { left: 105px; top: 286px; width: 296px; height: 254px;
    background: radial-gradient(ellipse at 60% 55%, var(--photo-tan), #4e3a2c 55%, var(--photo-green) 80%); }
  .photo-walking { left: 492px; top: 493px; width: 302px; height: 254px;
    background: linear-gradient(180deg, #6d8a5a 0%, #4f6b3a 45%, var(--photo-blonde) 46%, #d9c3a4 70%, #5c9a3a 72%); }
  .photo-home { left: 101px; top: 720px; width: 296px; height: 254px;
    background: linear-gradient(180deg, #f2efe9 0%, #ece6dc 35%, var(--photo-tan) 60%, #8a6a48 100%); }
  .service-label {
    position: absolute;
    font-weight: 800;
    font-size: 48px;
    line-height: 1;
    color: var(--white);
    letter-spacing: 1px;
    text-shadow: 2px 3px 3px rgba(20,30,50,0.55);
  }
  .label-minding { left: 437px; top: 393px; }
  .label-walking { left: 88px; top: 607px; }
  .label-home { left: 425px; top: 839px; }
  .contact-web {
    position: absolute;
    left: 196px; top: 1046px;
    display: flex; align-items: center; gap: 16px;
    font-weight: 300;
    font-size: 31px;
    color: var(--grey-text);
  }
  .contact-call {
    position: absolute;
    left: 100px; top: 1103px;
    color: var(--ocean);
    text-align: center;
  }
  .contact-call-title { font-weight: 700; font-size: 29px; line-height: 1.1; }
  .contact-call-phone { font-weight: 400; font-size: 32px; line-height: 1.15; letter-spacing: 1px; }
  .contact-social {
    position: absolute;
    left: 476px; top: 1117px;
    display: flex; align-items: center; gap: 16px;
    font-weight: 400;
    font-size: 29px;
    color: var(--grey-text);
  }
  .social-dot { width: 36px; height: 36px; border-radius: 50%; background: var(--grey-text); }
</style>
</head>
<body>
<main class="poster">
  <svg class="poster-bands" width="872" height="1200" viewBox="0 0 872 1200" aria-hidden="true">
    <rect width="872" height="1200" fill="var(--white)"/>
    <path d="M0 195 C 250 270, 560 290, 872 222 L872 1200 L0 1200 Z" fill="var(--sky)"/>
    <path d="M0 690 C 230 760, 560 750, 872 662 L872 1200 L0 1200 Z" fill="var(--ocean)"/>
    <path d="M0 1078 C 300 1040, 600 1010, 872 985 L872 1200 L0 1200 Z" fill="var(--white)"/>
  </svg>

  <header class="brand">
    <div class="brand-mark" aria-hidden="true"></div>
    <div class="brand-text">
      <span class="brand-name">Paw Haven</span>
      <span class="brand-tagline">PET SERVICES</span>
    </div>
  </header>

  <div class="service-photo photo-minding" role="img" aria-label="Photo of a merle-coated dog looking up, for dog minding"></div>
  <div class="service-photo photo-walking" role="img" aria-label="Photo of a bulldog on a leash standing on grass, for dog walking"></div>
  <div class="service-photo photo-home" role="img" aria-label="Photo of a small terrier sitting on a home doormat, for home visits"></div>

  <h2 class="service-label label-minding">DOG MINDING</h2>
  <h2 class="service-label label-walking">DOG WALKING</h2>
  <h2 class="service-label label-home">HOME VISIT</h2>

  <div class="contact-web">
    <svg width="44" height="44" viewBox="0 0 44 44" aria-hidden="true" fill="none" stroke="var(--grey-text)" stroke-width="2.5">
      <circle cx="22" cy="22" r="19"/>
      <ellipse cx="22" cy="22" rx="8" ry="19"/>
      <line x1="3" y1="22" x2="41" y2="22"/>
      <path d="M7 12 H37 M7 32 H37"/>
    </svg>
    <span>www.pawhavenexample.com.au</span>
  </div>

  <div class="contact-call">
    <div class="contact-call-title">Contact Us Today</div>
    <div class="contact-call-phone">0400 123 456</div>
  </div>

  <div class="contact-social">
    <span class="social-dot" aria-hidden="true"></span>
    <span>pawhavenexampleau</span>
  </div>
</main>
</body>
</html>
```